Post storm repair flyer

looking for an eye catching 6x9 postcard to send out to single family home owners advertising a "Post Storm Repair Special" explaining that after the recent hurricanes its very important to have your roof checked and any repairs fixed right away before they become a bigger more costly problem and that even though your home wasn't directly hit by the storm the high wind gust could've cause unseen damage.
offer $200 off any repair *some rules may apply
Crest Roofing
877.512.TOPS
www.CrestRoofingco.example

```html
<!DOCTYPE html>
<html lang="en">
<head>
<meta charset="utf-8">
<title>Crest Roofing – Post Storm Repair Special Postcard</title>
<link href="https://fonts.googleapis.com/css2?family=Lato:wght@400;700;900&display=swap" rel="stylesheet">
<style>
  :root{
    --gold:#f7b500;
    --gold-soft:#e9b43b;
    --ink:#111111;
    --paper:#ffffff;
    --backdrop:#c9c9c9;
    --roof-dark:#2b2b2e;
    --roof-mid:#6b6a70;
    --sky:#c9ced8;
  }
  *{box-sizing:border-box;margin:0;padding:0}
  html,body{width:1200px;height:2946px;overflow:hidden}
  body{background:var(--backdrop);font-family:"Lato",Arial,sans-serif;color:var(--ink);position:relative}
  .card{position:absolute;left:90px;width:1020px;height:720px;background:var(--paper);overflow:hidden;box-shadow:0 22px 40px rgba(0,0,0,.35)}
  .card--front{top:500px}
  .card--back{top:1720px}
  .card__art{position:absolute;inset:0;width:100%;height:100%}
  .brand{position:absolute;display:flex;align-items:center;gap:8px;font-weight:700;font-size:15px;letter-spacing:.5px;color:var(--ink)}
  .brand__mark{width:12px;height:12px;background:var(--gold)}
  .card--front .brand{left:52px;top:60px}

  .headline{position:absolute;left:40px;top:150px;line-height:.92;font-weight:900;text-transform:uppercase}
  .headline__post{display:block;color:var(--gold);font-size:66px}
  .headline__storm{display:block;font-size:92px;letter-spacing:-1px}
  .headline__repair{display:block;font-size:48px}
  .headline__repair em{font-style:normal;color:var(--gold)}
  .subhead{position:absolute;left:44px;top:378px;font-weight:700;font-size:16px;line-height:1.25}
  .intro{position:absolute;left:42px;top:430px;width:400px;font-size:12px;line-height:1.25}
  .offer{position:absolute;left:36px;top:470px;line-height:.95;text-transform:uppercase}
  .offer__label{display:block;font-weight:900;font-size:58px}
  .offer__amount{display:block;font-weight:900;font-size:78px;color:var(--gold)}
  .offer__scope{display:block;font-size:54px;font-weight:400}
  .offer__scope b{font-weight:900}

  .contact{position:absolute;text-align:right}
  .card--front .contact{right:38px;top:568px;color:var(--paper)}
  .contact__call{display:block;font-weight:900;font-size:26px;color:var(--gold)}
  .contact__phone{display:block;font-weight:900;font-size:52px;line-height:1.05}
  .contact__web{display:block;font-weight:700;font-size:19px;letter-spacing:1px}
  .contact__web span{color:var(--gold)}

  .process{position:absolute;left:52px;top:56px;width:470px}
  .process__title{font-weight:900;font-size:50px;line-height:.95;text-transform:uppercase;margin-bottom:26px}
  .process__list{list-style:none}
  .process__item{display:flex;gap:12px;font-size:22px;line-height:1.22;margin-bottom:22px}
  .process__num{flex:none;width:22px;height:22px;border-radius:50%;background:var(--ink);color:var(--paper);font-size:12px;font-weight:900;display:flex;align-items:center;justify-content:center;margin-top:4px}
  .process__item b{font-weight:900}
  .card--back .contact{left:54px;top:566px;text-align:left;color:var(--paper)}
  .card--back .contact__call{color:var(--paper);font-size:25px}
  .card--back .contact__phone{color:var(--gold);font-size:54px}
  .card--back .contact__web{font-size:19px}
  .card--back .brand{left:600px;top:120px}

  .postage{position:absolute;right:52px;top:54px;width:112px;border:1.5px solid #555;padding:4px 0;text-align:center;font-family:Arial,Helvetica,sans-serif;font-weight:700;font-size:12px;line-height:1.22}
  .address{position:absolute;left:628px;top:290px;width:338px;height:106px;border:1.5px solid #333;padding:28px 34px;font-family:Arial,Helvetica,sans-serif;font-size:18px;line-height:1.25}
</style>
</head>
<body>

<section class="card card--front" aria-label="Postcard front">
  <svg class="card__art" viewBox="0 0 1020 720" preserveAspectRatio="none">
    <defs>
      <linearGradient id="roofPhoto" x1="0" y1="0" x2="0.6" y2="1">
        <stop offset="0" stop-color="var(--sky)"/>
        <stop offset=".2" stop-color="#8d8c92"/>
        <stop offset=".6" stop-color="var(--roof-mid)"/>
        <stop offset="1" stop-color="#4a494e"/>
      </linearGradient>
    </defs>
    <polygon role="img" aria-label="Photo of a roofer in a safety harness repairing shingles on a roof" points="355,0 1020,0 1020,720 560,720 430,330" fill="url(#roofPhoto)"/>
    <polygon points="560,720 1020,720 1020,430 760,520 620,620" fill="var(--roof-dark)" opacity=".92"/>
    <polygon points="470,420 488,410 590,720 556,720" fill="var(--gold)"/>
    <polygon points="150,720 470,620 500,620 540,720" fill="var(--ink)"/>
    <polygon points="220,720 430,640 450,645 270,720" fill="var(--gold)"/>
  </svg>

  <div class="brand"><span class="brand__mark"></span>CREST ROOFING</div>

  <h1 class="headline">
    <span class="headline__post">Post</span>
    <span class="headline__storm">Storm</span>
    <span class="headline__repair">Repair <em>Special</em></span>
  </h1>
  <p class="subhead">Protect Your Home with a Roof Inspection<br>After the Storm</p>
  <p class="intro">Don't wait until the damage is visible or more severe.<br>A quick inspection now can save you from expensive repairs later on. Stay proactive and protect your home!</p>
  <p class="offer" style="top:475px">
    <span class="offer__label">Offer</span>
    <span class="offer__amount">$200 Off</span>
    <span class="offer__scope">Any <b>Repair</b></span>
  </p>

  <p class="contact">
    <span class="contact__call">CALL US TODAY</span>
    <span class="contact__phone">877.512.TOPS</span>
    <span class="contact__web">www.<span>CrestRoofingco</span>.example</span>
  </p>
</section>

<section class="card card--back" aria-label="Postcard back">
  <svg class="card__art" viewBox="0 0 1020 720" preserveAspectRatio="none">
    <defs>
      <linearGradient id="fadedPhoto" x1="0" y1="0" x2="0" y2="1">
        <stop offset="0" stop-color="#ffffff"/>
        <stop offset="1" stop-color="#dcdcdc"/>
      </linearGradient>
    </defs>
    <polygon role="img" aria-label="Faded photo of a roofer working on shingles" points="480,420 1020,420 1020,720 450,720" fill="url(#fadedPhoto)"/>
    <polygon points="0,0 618,0 460,720 0,720" fill="var(--gold-soft)"/>
    <polygon points="0,460 450,600 424,720 0,720" fill="var(--ink)"/>
    <polygon points="478,570 492,570 448,720 430,720" fill="var(--gold)"/>
  </svg>

  <div class="process">
    <h2 class="process__title">Crest Roofing<br>Process</h2>
    <ol class="process__list">
      <li class="process__item"><span class="process__num">1</span><span>Complimentary consultation to access your roofing needs and review our honest recommendations.</span></li>
      <li class="process__item"><span class="process__num">2</span><span>Our team of professionals replace, restore, or repair your roof making the process as stress-free as possible.</span></li>
      <li class="process__item"><span class="process__num">3</span><span><b>100% SATISFACTION</b>, peace of mind, and continued professional coverage backed by CREST Protection*.</span></li>
    </ol>
  </div>

  <p class="contact">
    <span class="contact__call">CALL US TODAY</span>
    <span class="contact__phone">877.512.TOPS</span>
    <span class="contact__web">www.CrestRoofingco.example</span>
  </p>

  <div class="brand"><span class="brand__mark"></span>CREST ROOFING</div>

  <div class="postage">PRSRT STD<br>ECRWSS<br>U.S.POSTAGE<br><span style="font-size:14px">PAID</span><br>EDDM Retail</div>

  <div class="address">Local<br>Postal Customer</div>
</section>

</body>
</html>
```